Dental Practice Website design

Design a new website for Bramblewick Dental Practice.
Design should be warm, neutral in colour, with some small amount of bright colour if needed but kept to a minimum. Website should look professional, high end. Home page should be easy to navigate and simple for patients to be able to book online.
Logo in files along with some examples of websites that we like. Please ask if any further info needed.
Menu should have:
About
New Patients
Treatments
Fees
Contact Us
Updates

Industry/Entity Type

Dentistry

Number of Pages Required

4 page

Font styles to use
Sans Serif

Colors

Designer to choose colors to be used in the design.

Requirements
Must have
• google reviews badge, book online button,
Nice to have
• neutral, relaxing colours
Should not have
• harsh, bright colours!

```html
<!DOCTYPE html>
<html lang="en">
<head>
<meta charset="utf-8">
<title>Bramblewick Dental Practice</title>
<link href="https://fonts.googleapis.com/css2?family=Montserrat:wght@400;500;600;700&display=swap" rel="stylesheet">
<style>
:root{
  --blue:#2a7fcf;
  --ink:#111;
  --black:#000;
  --white:#fff;
  --pale:#f3f7f9;
  --text:#222;
  --muted:#666;
  --line:#cfd8de;
  --star:#e9b23a;
}
*{box-sizing:border-box;margin:0;padding:0}
html,body{width:1200px;height:4167px;overflow:hidden}
body{font-family:"Montserrat",sans-serif;color:var(--text);background:var(--white);position:relative}
.abs{position:absolute}
section,header,footer{position:absolute;left:0;width:1200px;overflow:hidden}
.h2{font-size:46px;font-weight:700;color:var(--ink);line-height:1.15}
.small{font-size:12.5px;line-height:1.55}
.btn{position:absolute;background:var(--blue);color:var(--white);border-radius:20px;font-size:14px;display:flex;align-items:center;justify-content:center}
.photo{position:absolute}

/* header */
.site-header{top:0;height:113px;background:var(--black)}
.brand{position:absolute;display:flex;align-items:center;gap:10px;color:var(--white);font-weight:500;letter-spacing:1px}
.brand-mark{width:22px;height:22px;border:2px solid var(--white)}
.brand-name{font-size:13px;line-height:1.3;text-transform:uppercase}
.nav{position:absolute;top:46px;left:531px;color:var(--white);font-size:15px}
.nav span{position:absolute;white-space:nowrap}
.nav-cta{position:absolute;left:1007px;top:39px;width:136px;height:36px;background:var(--white);color:var(--blue);border-radius:18px;font-size:15px;display:flex;align-items:center;justify-content:center}

/* hero */
.hero{top:113px;height:479px;background:linear-gradient(90deg,#f6f6f6 0%,#eef0f1 45%,#d9d4d0 100%)}
.hero-photo{left:560px;top:0;width:640px;height:479px;background:radial-gradient(ellipse at 60% 40%,#e8c7b3 0%,#d9c2b4 30%,#e4e6e8 70%,#eef0f1 100%)}
.hero-title{position:absolute;left:57px;top:112px;font-size:58px;font-weight:700;line-height:1.17;color:var(--ink)}
.hero-title .accent{color:var(--blue)}
.hero-text{left:57px;top:265px;width:470px}

/* about */
.about{top:592px;height:513px;background:var(--pale)}
.about-photo{left:55px;top:78px;width:485px;height:355px;border-radius:24px;background:linear-gradient(135deg,#efe3da 0%,#e2cbbd 50%,#c98f86 100%)}
.about-text{left:638px;width:505px}

/* treatments */
.treatments{top:1105px;height:588px;background:linear-gradient(120deg,#4a4e52 0%,#6b6e71 45%,#3f4245 100%)}
.arrow-btn{position:absolute;width:38px;height:38px;border-radius:50%;display:flex;align-items:center;justify-content:center}
.card{position:absolute;top:150px;width:349px;height:381px;background:var(--white)}
.card-title{position:absolute;left:22px;top:30px;font-size:23px;font-weight:700;color:var(--ink)}
.card-go{position:absolute;right:20px;top:20px;width:40px;height:40px;border-radius:50%;background:var(--black);display:flex;align-items:center;justify-content:center}
.card-text{position:absolute;left:26px;top:78px;width:290px;font-size:12.5px;line-height:1.55}
.card-photo{position:absolute;left:26px;top:183px;width:297px;height:170px}

/* new patients */
.patients{top:1693px;height:540px;background:var(--white)}
.check-list{position:absolute;left:57px;top:250px;list-style:none}
.check-list li{display:flex;align-items:center;gap:16px;font-size:17px;font-weight:500;color:var(--ink);height:38px}

/* schedule */
.schedule{top:2233px;height:510px;background:linear-gradient(90deg,#fff 0%,#f4f8fa 100%)}

/* testimonials */
.reviews{top:2743px;height:600px;background:linear-gradient(180deg,#2e3032 0%,#55585b 60%,#3c3e40 100%)}
.review{position:absolute;top:122px;width:353px;height:413px;background:var(--white)}
.avatar{position:absolute;left:29px;top:28px;width:84px;height:84px;border-radius:50%}
.review-name{position:absolute;left:133px;top:58px;font-size:19px;font-weight:600;color:var(--ink)}
.review-text{position:absolute;left:29px;top:148px;width:300px;font-size:12.5px;line-height:1.5}
.rating{position:absolute;left:33px;top:330px;display:flex;align-items:center;gap:8px}
.badge-dot{width:22px;height:22px;border-radius:50%;border:3px solid var(--blue)}
.review-date{position:absolute;left:37px;top:371px;font-size:12.5px;color:var(--muted)}

/* contact */
.contact{top:3343px;height:520px;background:var(--pale)}
.contact-item{position:absolute;left:55px;display:flex;align-items:center;gap:32px;font-size:21px;color:var(--ink)}
.contact-icon{width:45px;height:45px;border-radius:50%;background:var(--blue);display:flex;align-items:center;justify-content:center;flex:none}
.field{position:absolute;height:35px;border:1px solid var(--line);border-radius:18px;background:var(--white);font-size:12px;color:#999;padding:10px 16px}
.field.area{border-radius:4px;height:118px;padding:14px 18px}

/* footer */
.site-footer{top:3863px;height:304px;background:var(--black);color:var(--white)}
.foot-col{position:absolute;top:48px}
.foot-col h4{font-size:16px;font-weight:600;color:var(--blue);margin-bottom:14px}
.foot-col p{font-size:12.5px;line-height:26px}
.social{position:absolute;top:88px;left:920px;display:flex;gap:10px}
.social span{width:29px;height:29px;border-radius:50%;background:var(--white);border:3px solid var(--blue)}
.foot-line{position:absolute;left:0;top:257px;width:1200px;height:1px;background:#333}
.copyright{position:absolute;top:272px;width:1200px;text-align:center;font-size:12.5px}
</style>
</head>
<body>

<header class="site-header">
  <div class="brand" style="left:55px;top:30px">
    <span class="brand-mark"></span>
    <span class="brand-name">Bramblewick<br>Dental Practice</span>
  </div>
  <nav class="nav">
    <span style="left:0">Home</span>
    <span style="left:78px">About</span>
    <span style="left:157px">New Patients</span>
    <span style="left:289px">Treatments</span>
    <span style="left:411px">Fees</span>
  </nav>
  <div class="nav-cta">Contact Us</div>
</header>

<section class="hero">
  <div class="photo hero-photo" role="img" aria-label="Smiling woman in the dental chair during a check-up"></div>
  <h1 class="hero-title"><span class="accent">Gentle Dentistry for</span><br>a Lifetime <span class="accent">of Smiles</span></h1>
  <p class="abs small hero-text">Welcome to our friendly dental practice nestled in the heart of beautiful Hollowmere, UK. Our team of dedicated dentists, hygienists and support staff are here to provide you with exceptional dental care.</p>
  <div class="btn" style="left:57px;top:342px;width:224px;height:33px">Book an Appointment</div>
</section>

<section class="about">
  <div class="photo about-photo" role="img" aria-label="Illustration pairing a smiling patient in the chair with a close-up of dental treatment"></div>
  <h2 class="abs h2 about-text" style="top:66px">About</h2>
  <p class="abs small about-text" style="top:145px">Welcome to our friendly dental practice nestled in the heart of beautiful Hollowmere, UK. Our team of dedicated dentists, hygienists and support staff are here to provide you with exceptional dental care. With a wide array of services, including general and cosmetic dentistry, orthodontics and emergency care, we're confident that we can deliver the highest quality treatment to you and your loved ones.</p>
  <p class="abs small about-text" style="top:280px">At our practice, we believe that a visit to the dentist should be a comfortable and positive experience. We strive to create a warm and welcoming atmosphere where our patients can feel at ease and confident in the care they receive. Our state-of-the-art facilities and equipment mean that you can trust us to deliver the latest techniques and treatments to ensure your oral health is at its best.</p>
  <div class="btn" style="left:638px;top:416px;width:138px;height:34px">Know More</div>
</section>

<section class="treatments" role="img" aria-label="Dentist treating a patient, softly darkened behind the cards">
  <h2 class="abs h2" style="left:57px;top:54px;color:var(--white)">Treatments</h2>
  <div class="arrow-btn" style="left:1050px;top:64px;background:var(--black)"><svg width="18" height="12" viewBox="0 0 18 12"><path d="M17 6H2M7 1 2 6l5 5" fill="none" stroke="#fff" stroke-width="1.6"/></svg></div>
  <div class="arrow-btn" style="left:1098px;top:64px;background:var(--white)"><svg width="18" height="12" viewBox="0 0 18 12"><path d="M1 6h15M11 1l5 5-5 5" fill="none" stroke="#2a7fcf" stroke-width="1.6"/></svg></div>

  <div class="card" style="left:57px">
    <div class="card-title" style="color:var(--blue)">Dental Fillings</div>
    <div class="card-go" style="background:var(--blue)"><svg width="14" height="14" viewBox="0 0 14 14"><path d="M2 12 12 2M5 2h7v7" fill="none" stroke="#fff" stroke-width="1.5"/></svg></div>
    <p class="card-text">Lorem ipsum dolor sit amet, cons ectetuer adipiscing elit, sed diam nonummy nibh euismod tincidunt ut laoreet dolore magna aliquam erat volutpat. Ut wisi enim</p>
    <div class="card-photo" role="img" aria-label="Patient smiling while a dentist checks her teeth" style="background:linear-gradient(135deg,#d9c4b6,#f1ebe6 60%,#b7c9d8)"></div>
  </div>
  <div class="card" style="left:425px">
    <div class="card-title">Teeth Whitening</div>
    <div class="card-go"><svg width="14" height="14" viewBox="0 0 14 14"><path d="M2 12 12 2M5 2h7v7" fill="none" stroke="#fff" stroke-width="1.5"/></svg></div>
    <p class="card-text">Lorem ipsum dolor sit amet, cons ectetuer adipiscing elit, sed diam nonummy nibh euismod tincidunt ut laoreet dolore magna aliquam erat volutpat. Ut wisi enim</p>
    <div class="card-photo" role="img" aria-label="Close-up of a bright smile with dental mirror" style="background:linear-gradient(135deg,#7d9cbf,#c98a80 55%,#f2e6e2)"></div>
  </div>
  <div class="card" style="left:794px">
    <div class="card-title">Clear Aligners</div>
    <div class="card-go"><svg width="14" height="14" viewBox="0 0 14 14"><path d="M2 12 12 2M5 2h7v7" fill="none" stroke="#fff" stroke-width="1.5"/></svg></div>
    <p class="card-text">Lorem ipsum dolor sit amet, cons ectetuer adipiscing elit, sed diam nonummy nibh euismod tincidunt ut laoreet dolore magna aliquam erat volutpat. Ut wisi enim</p>
    <div class="card-photo" role="img" aria-label="Gloved hands holding a dental model with braces" style="background:linear-gradient(135deg,#f3f4f6,#e3b4a6 50%,#a9c3dc)"></div>
  </div>
</section>

<section class="patients">
  <h2 class="abs h2" style="left:57px;top:98px">New Patients</h2>
  <p class="abs small" style="left:57px;top:180px;width:505px">Welcome to [Your Dental Clinic Name]! We are thrilled to welcome new patients to our practice. To make your first visit as smooth as possible, we have provided some helpful information below</p>
  <ul class="check-list">
    <li><svg width="22" height="22" viewBox="0 0 22 22"><rect x="1" y="3" width="18" height="18" rx="2" fill="none" stroke="#2a7fcf" stroke-width="1.4"/><path d="M5 11l4 4 11-12" fill="none" stroke="#2a7fcf" stroke-width="1.6"/></svg>New Patient Forms</li>
    <li><svg width="22" height="22" viewBox="0 0 22 22"><rect x="1" y="3" width="18" height="18" rx="2" fill="none" stroke="#2a7fcf" stroke-width="1.4"/><path d="M5 11l4 4 11-12" fill="none" stroke="#2a7fcf" stroke-width="1.6"/></svg>What to Expect</li>
    <li><svg width="22" height="22" viewBox="0 0 22 22"><rect x="1" y="3" width="18" height="18" rx="2" fill="none" stroke="#2a7fcf" stroke-width="1.4"/><path d="M5 11l4 4 11-12" fill="none" stroke="#2a7fcf" stroke-width="1.6"/></svg>Insurance Information</li>
  </ul>
  <div class="btn" style="left:57px;top:384px;width:164px;height:33px">Know More</div>
  <div class="photo" role="img" aria-label="Smiling woman in a dental chair with a dentist's instruments" style="left:648px;top:62px;width:552px;height:442px;background:linear-gradient(135deg,#d6dadc 0%,#e6c8b6 45%,#b9cfd6 100%)"></div>
</section>

<section class="schedule">
  <div class="photo" role="img" aria-label="Happy family lying on a rug with their dog" style="left:0;top:0;width:552px;height:440px;background:linear-gradient(135deg,#e9e5df 0%,#c8b6a4 50%,#b59a7e 100%)"></div>
  <h2 class="abs h2" style="left:643px;top:96px">Schedule Your New<br>Patient Appointment</h2>
  <p class="abs small" style="left:643px;top:236px;width:505px">We take the time to listen to your concerns, answer your questions, and develop a treatment plan that aligns with your specific goals<br>&nbsp;and budget.</p>
  <div class="btn" style="left:648px;top:320px;width:156px;height:33px">book online</div>
</section>

<section class="reviews" role="img" aria-label="Dental clinic interior, darkened behind the reviews">
  <h2 class="abs h2" style="left:0;width:1200px;top:34px;text-align:center;color:var(--white)">What our client says about us</h2>

  <div class="review" style="left:57px">
    <div class="avatar" role="img" aria-label="Reviewer portrait" style="background:linear-gradient(135deg,#888,#333)"></div>
    <div class="review-name">Elowen</div>
    <p class="review-text">Lorem ipsum dolor sit amet, consectetuer adipiscing elit, sed diam nonummy nibh euismod tincidunt ut laoreet dolore magna aliquam erat volutpat. Ut wisi enim ad minim veniamLorem ipsum dolor sit amet, consectetuer adipiscing elit, sed diam nonummy nibh euismod tincidunt ut laoreet dolore magna aliquam erat volutpat. Ut wisi enim ad minim veniam</p>
    <div class="rating"><span class="badge-dot"></span><svg width="95" height="16" viewBox="0 0 95 16" fill="var(--star)"><path id="st" d="M8 0l2.4 5 5.4.6-4 3.7 1.1 5.4L8 12l-4.9 2.7 1.1-5.4-4-3.7L5.6 5z"/><use href="#st" x="26"/><use href="#st" x="52"/><use href="#st" x="78"/></svg></div>
    <div class="review-date">06/11/2024</div>
  </div>
  <div class="review" style="left:423px">
    <div class="avatar" role="img" aria-label="Reviewer portrait" style="background:linear-gradient(135deg,#e6c2ad,#8a5a45)"></div>
    <div class="review-name">Tamsin</div>
    <p class="review-text">Lorem ipsum dolor sit amet, consectetuer adipiscing elit, sed diam nonummy nibh euismod tincidunt ut laoreet dolore magna aliquam erat volutpat. Ut wisi enim ad minim veniamLorem ipsum dolor sit amet, consectetuer adipiscing elit, sed diam nonummy nibh euismod tincidunt ut laoreet dolore magna</p>
    <div class="rating"><span class="badge-dot"></span><svg width="95" height="16" viewBox="0 0 95 16" fill="var(--star)"><use href="#st"/><use href="#st" x="26"/><use href="#st" x="52"/><use href="#st" x="78"/></svg></div>
    <div class="review-date">02/10/2023</div>
  </div>
  <div class="review" style="left:790px">
    <div class="avatar" role="img" aria-label="Reviewer portrait" style="background:linear-gradient(135deg,#6b5b50,#1c1c1c)"></div>
    <div class="review-name">Tamsin Elowen</div>
    <p class="review-text">Lorem ipsum dolor sit amet, consectetuer adipiscing elit, sed diam nonummy nibh euismod tincidunt ut laoreet dolore magna aliquam erat volutpat. Ut wisi enim ad minim veniamLorem ipsum dolor sit amet, consectetuer adipiscing elit, sed diam nonummy nibh euismod tincidunt ut laoreet dolore magna aliquam erat volutpat.</p>
    <div class="rating"><span class="badge-dot"></span><svg width="95" height="16" viewBox="0 0 95 16" fill="var(--star)"><use href="#st"/><use href="#st" x="26"/><use href="#st" x="52"/><use href="#st" x="78"/></svg></div>
    <div class="review-date">12/04/2024</div>
  </div>

  <svg class="abs" style="left:576px;top:574px" width="48" height="10" viewBox="0 0 48 10"><circle cx="5" cy="5" r="4" fill="#fff"/><circle cx="24" cy="5" r="4" fill="#2a7fcf"/><circle cx="43" cy="5" r="4" fill="#fff"/></svg>
</section>

<section class="contact">
  <h2 class="abs h2" style="left:55px;top:72px">Contact</h2>
  <div class="contact-item" style="top:170px"><span class="contact-icon"><svg width="20" height="20" viewBox="0 0 24 24"><path d="M6.6 10.8a15 15 0 0 0 6.6 6.6l2.2-2.2a1 1 0 0 1 1-.25 11.4 11.4 0 0 0 3.6.6 1 1 0 0 1 1 1V20a1 1 0 0 1-1 1A17 17 0 0 1 3 4a1 1 0 0 1 1-1h3.5a1 1 0 0 1 1 1c0 1.25.2 2.45.6 3.6a1 1 0 0 1-.25 1z" fill="#fff"/></svg></span>0123 456 789</div>
  <div class="contact-item" style="top:247px"><span class="contact-icon"><svg width="20" height="16" viewBox="0 0 20 16"><rect x="1" y="1" width="18" height="14" rx="2" fill="#fff"/><path d="M1 2l9 7 9-7" fill="none" stroke="#2a7fcf" stroke-width="1.6"/></svg></span>info@bramblewickdental.com</div>
  <div class="contact-item" style="top:322px;line-height:1.45"><span class="contact-icon"><svg width="18" height="22" viewBox="0 0 18 22"><path d="M9 1a7 7 0 0 0-7 7c0 5 7 13 7 13s7-8 7-13a7 7 0 0 0-7-7z" fill="#fff"/><circle cx="9" cy="8" r="2.6" fill="#2a7fcf"/></svg></span>Lorem ipsum dolor sit amet,<br>consectetuer , 09873</div>

  <h2 class="abs h2" style="left:640px;width:510px;top:40px;text-align:center">Let's Talk About<br>Your Smile</h2>
  <div class="field" style="left:636px;top:192px;width:250px">First Name</div>
  <div class="field" style="left:896px;top:192px;width:250px">Last Name</div>
  <div class="field" style="left:636px;top:240px;width:250px">E - Mail</div>
  <div class="field" style="left:896px;top:240px;width:250px">Subject</div>
  <div class="field area" style="left:636px;top:287px;width:508px">Message...</div>
  <div class="btn" style="left:636px;top:429px;width:510px;height:33px;font-size:13px">Schedule Your Appointment Today</div>
</section>

<footer class="site-footer">
  <div class="brand" style="left:65px;top:70px">
    <span class="brand-mark"></span>
    <span class="brand-name">Bramblewick<br>Dental Practice</span>
  </div>
  <p class="abs" style="left:57px;top:165px;width:240px;font-size:12.5px;line-height:1.5">we believe that a visit to the dentist should be a comfortable and positive experience.</p>
  <div class="foot-col" style="left:405px"><h4>Quick links</h4><p>Home<br>About<br>New Patients<br>Treatments<br>Fees</p></div>
  <div class="foot-col" style="left:655px"><h4>IV Treatment</h4><p>Dental Fillings<br>Teeth Whitening<br>Clear Aligners<br>Kids Dentistry<br>Teeth Implants</p></div>
  <div class="foot-col" style="left:920px"><h4>Social Media</h4></div>
  <div class="social"><span></span><span></span><span></span><span></span></div>
  <div class="foot-line"></div>
  <div class="copyright">Copyright © 2025 bramblewickdental All rights reserved.</div>
</footer>

</body>
</html>
```